Print design needed to improve the layout and look of some existing documents

We need someone to take a couple of existing documents that we have and make them look much better using our existing logo and corporate colors etc. We require these to be delivered in a format that will allow our staff to edit the content as necessary via Microsoft word for conversion once finalized into a PDF. Ideally, we will also be able to use this as a newsletter template or for other documents that might be required in our business. www.larchfieldcapital.com.au
Updates

Project Deadline Extended Reason: So far, I have only seen one design that I believe is quite good quality. Added Sunday, July 3, 2016

Target Market(s)

Business owners, executives, retirees

Industry/Entity Type

Financial Service

Font styles to use
Serif

Requirements
Must have
• Design that uses our existing branding and colors. It also needs to be ina form that we can edit the content / update easily. Ideally the format / layout could also be used for other documents such as short newsletters etc.
Nice to have
• Fresh, simple and crisp. Very professional looking.
Should not have
• strange fonts, weird layouts.

```html
<!DOCTYPE html>
<html lang="en">
<head>
<meta charset="utf-8">
<title>Privacy Policy Statement – Larchfield Capital</title>
<link href="https://fonts.googleapis.com/css2?family=Carlito:wght@400;700&display=swap" rel="stylesheet">
<style>
:root{
  --top-bar:#1f9ad6;
  --page-tint:#ddedf9;
  --heading:#2b7fc6;
  --body-text:#1e1e1e;
  --brand-grey:#7a7d80;
  --brand-mark:#2a9fd8;
  --footer-text:#8a8a8a;
  --link:#1a4fd6;
  --icon-blue:#2a9fd8;
  --icon-green:#7cc242;
}
*{box-sizing:border-box;margin:0;padding:0}
html,body{width:849px;height:1200px;overflow:hidden}
body{font-family:"Carlito","Calibri",Arial,sans-serif;color:var(--body-text);background:var(--page-tint);position:relative}
.top-bar{position:absolute;left:0;top:0;width:849px;height:8px;background:var(--top-bar)}
.page-header{position:absolute;left:0;top:8px;width:849px;height:89px;background:#fff;display:flex;align-items:center;justify-content:center;gap:12px;box-shadow:0 1px 3px rgba(0,0,0,.08)}
.brand-dot{width:26px;height:26px;border-radius:50%;background:var(--brand-mark)}
.brand-name{font-size:30px;font-weight:400;letter-spacing:2px;color:var(--brand-grey)}
.policy-body{position:absolute;left:103px;top:122px;width:643px;font-size:15.4px;line-height:19px;text-align:justify}
.policy-body p{margin-bottom:19px}
.policy-body h2{font-size:15.4px;font-weight:700;color:var(--heading);line-height:19px}
.policy-body a{color:var(--link)}
.version-note{position:absolute;right:103px;top:1041px;font-size:15.4px;line-height:19px}
.page-footer{position:absolute;left:0;top:1128px;width:849px;height:72px;background:#fff;color:var(--footer-text);font-size:11px;font-weight:700;text-align:center;padding-top:10px;line-height:18.5px}
.footer-row{display:flex;justify-content:center;align-items:center;gap:10px}
.footer-item{display:inline-flex;align-items:center;gap:5px}
.footer-item svg{width:13px;height:13px}
</style>
</head>
<body>
<div class="top-bar"></div>
<header class="page-header">
  <span class="brand-dot"></span>
  <span class="brand-name">LARCHFIELD CAPITAL</span>
</header>

<main class="policy-body">
  <p>We also maintain physical security over our paper and electronic data and premises, by using locks and security systems.</p>

  <h2>Will we disclose the information we collect to anyone?</h2>
  <p>We do not sell, trade, or rent your personal information to others. We may disclose your information to third party organisations where you have request that we liaise with or refer you to the organisations. This may include firms providing investment, superannuation, accounting legal, credit, transactional banking or insurance services and may need to provide your information to contractors who supply services to us or to other companies in the event of a corporate sale, merger, reorganisation, dissolution or similar event. However, we will take all reasonable steps to ensure that they protect your information in the same way that we do.</p>
  <p>We may also provide your information to others if we are required to do so by law or under some unusual other circumstances which the Privacy Act permits. We will not provide your information to any overseas recipients unless we are required to by Law.</p>

  <h2>How can you check, update or change the information we are holding?</h2>
  <p>Upon receipt of your written request and enough information to allow us to identify the information, we will disclose to you the personal information we hold about you. We will also correct, amend or delete any personal information that we agree is inaccurate, irrelevant, out of date or incomplete.</p>
  <p>If you wish to access or correct your personal information please contact our office (see contact details below). We do not charge for receiving a request for access to personal information or for complying with a correction request.</p>
  <p>In some limited cases, we may need to refuse access to your information or refuse a request for correction. We will advise you as soon as possible after your request if this is the case and the reasons for our refusal.</p>

  <h2>What happens if you want to complain?</h2>
  <p>If you have any concerns about whether we have complied with the Privacy Act or this Privacy Policy when collecting of handling your personal information, you can call us on 08 6140 2758 or email your concerns to <a href="mailto:admin@larchfieldcapital.com.au">admin@larchfieldcapital.com.au</a>.</p>
  <p>We will consider any privacy related complaint through our internal complaints resolution process and we will try to respond with a decision within 45 days of you making the complaint.</p>

  <h2>Your consent</h2>
  <p>By asking us to assist with your financial needs, you consent to the collection and use of the information you have provided to us for the purposes described above.</p>

  <h2>Tell us what you think</h2>
  <p>We welcome your questions and comments about privacy. If you have any concerns or complaints, please contact us on 08 6140 2758 or via email on <a href="mailto:admin@larchfieldcapital.com.au">admin@larchfieldcapital.com.au</a>.</p>
</main>

<div class="version-note">Privacy Policy Statement – V2015</div>

<footer class="page-footer">
  <div class="footer-row">Larchfield Capital Pty Ltd &nbsp;|&nbsp; AFSL 478203 &nbsp;|&nbsp; ABN 52 611 903 174</div>
  <div class="footer-row">
    <span class="footer-item"><svg viewBox="0 0 14 14"><circle cx="7" cy="7" r="7" fill="var(--icon-blue)"/><path d="M3.5 7.2L7 4l3.5 3.2M4.6 6.6V10h4.8V6.6" fill="none" stroke="#fff" stroke-width="1.2"/></svg>14C Tallowood Road, Mount Harlow, WA 6157</span>
    <span class="footer-item"><svg viewBox="0 0 14 14"><circle cx="7" cy="7" r="7" fill="var(--icon-green)"/><rect x="3.5" y="4.5" width="7" height="5" fill="none" stroke="#fff" stroke-width="1.1"/><path d="M3.5 4.5L7 7.3l3.5-2.8" fill="none" stroke="#fff" stroke-width="1.1"/></svg>Po Box 2284, Ferndale Bridge, Westcove WA 6157</span>
  </div>
  <div class="footer-row">
    <span class="footer-item"><svg viewBox="0 0 14 14"><circle cx="7" cy="7" r="7" fill="var(--icon-green)"/><circle cx="7" cy="7" r="3.6" fill="none" stroke="#fff" stroke-width="1"/><path d="M3.4 7h7.2M7 3.4v7.2" stroke="#fff" stroke-width="0.9"/></svg>www.larchfieldcapital.com.au</span>
    <span class="footer-item"><svg viewBox="0 0 14 14"><circle cx="7" cy="7" r="7" fill="var(--icon-blue)"/><path d="M4.6 3.8l1.4-.3.8 1.8-.9.7c.4.9 1.1 1.6 2 2l.7-.9 1.8.8-.3 1.4c-3 .2-5.7-2.5-5.5-5.5z" fill="#fff"/></svg>08 6140 2758</span>
  </div>
</footer>
</body>
</html>
```